Bref créative
Stationary Package for Larkmont Homes LLC
Business Card, Letterhead, envelope, fax, invoice, folder, yard marketing signage
Professional
Owen Talbert
PO Box 318264
Houston, TX 77019
larkmonthomes@quellmail.com
www.larkmonthomes.net

```html
<!DOCTYPE html>
<html lang="en">
<head>
<meta charset="utf-8">
<title>Larkmont Homes LLC – Stationery Package</title>
<link rel="stylesheet" href="https://fonts.googleapis.com/css2?family=Montserrat:wght@400;600&display=swap">
<style>
:root{
  --backdrop:#3b3b3b;
  --paper:#ffffff;
  --paper-edge:#e4e4e4;
  --brand-red:#c8432b;
  --brand-red-dark:#a8351f;
  --brand-grey:#8c8c8c;
  --brand-grey-dark:#6f6f6f;
  --ink:#555555;
  --faint:#f3dcd6;
}
*{box-sizing:border-box;margin:0;padding:0}
html,body{width:1200px;height:312px;overflow:hidden}
body{background:var(--backdrop);font-family:"Montserrat",sans-serif;color:var(--ink);position:relative}
.piece{position:absolute;background:var(--paper);box-shadow:0 1px 3px rgba(0,0,0,.45)}
.wordmark{display:flex;align-items:center;gap:3px;color:var(--brand-red);font-weight:600;white-space:nowrap}
.wordmark .mark-square{display:block;background:var(--brand-red)}
.wordmark.on-dark{color:#fff}
.wordmark.on-dark .mark-square{background:#fff}

/* business cards */
.card{width:84px;height:43px;padding:5px}
.card .wordmark{font-size:5px}
.card .wordmark .mark-square{width:5px;height:5px}
.card-front{display:flex;align-items:center;justify-content:center}
.card-front .wordmark{font-size:7px}
.card-front .wordmark .mark-square{width:7px;height:7px}
.card-back .details{font-size:3.2px;line-height:4.4px;margin-top:4px}
.card-back .details strong{color:var(--brand-red);font-weight:600}

/* letterheads */
.letterhead{width:209px;height:288px}
.letterhead .head{position:absolute;top:16px;left:0;right:0;display:flex;justify-content:center}
.letterhead .head .wordmark{font-size:8px}
.letterhead .head .wordmark .mark-square{width:8px;height:8px}
.letterhead .address{position:absolute;top:14px;right:14px;font-size:3.2px;line-height:4.4px;text-align:right}
.letterhead .faint-mark{position:absolute;left:50%;top:58%;transform:translate(-50%,-50%);color:var(--faint);font-size:15px}
.letterhead .faint-mark .mark-square{background:var(--faint);width:26px;height:26px}
.letterhead .footer{position:absolute;bottom:10px;left:0;right:0;text-align:center;font-size:3.2px}
.letterhead .side-rule{position:absolute;left:8px;top:150px;width:3px;height:26px;background:var(--brand-red)}

/* envelopes */
.envelope{width:197px;height:104px}
.envelope .corner{position:absolute;top:10px;left:10px}
.envelope .corner .wordmark{font-size:5px}
.envelope .corner .wordmark .mark-square{width:5px;height:5px}
.envelope .return{font-size:3px;line-height:4px;margin-top:2px}
.envelope .footer{position:absolute;bottom:8px;left:0;right:0;text-align:center;font-size:3.2px}

/* open-flap envelope stack */
.flap-stack{position:absolute;left:883px;top:24px;width:293px;height:218px}
.flap-stack svg{display:block}
.flap-stack .flap-logo{position:absolute;top:34px;left:0;right:0;display:flex;justify-content:center}
.flap-stack .flap-logo .wordmark{font-size:8px}
.flap-stack .flap-logo .wordmark .mark-square{width:8px;height:8px}
</style>
</head>
<body>

<!-- business cards -->
<div class="piece card card-front" style="left:24px;top:115px">
  <div class="wordmark"><span class="mark-square"></span>Larkmont Homes</div>
</div>
<div class="piece card card-back" style="left:115px;top:115px">
  <div class="wordmark"><span class="mark-square"></span>Larkmont Homes</div>
  <div class="details"><strong>Owen Talbert</strong><br>PO Box 318264<br>Houston, TX 77019</div>
</div>
<div class="piece card card-front" style="left:24px;top:168px">
  <div class="wordmark"><span class="mark-square"></span>Larkmont Homes</div>
</div>
<div class="piece card card-back" style="left:115px;top:168px">
  <div class="wordmark"><span class="mark-square"></span>Larkmont Homes</div>
  <div class="details"><strong>Owen Talbert</strong><br>larkmonthomes@quellmail.com<br>www.larkmonthomes.net</div>
</div>

<!-- letterheads -->
<div class="piece letterhead" style="left:223px;top:17px">
  <div class="head"><div class="wordmark"><span class="mark-square"></span>Larkmont Homes</div></div>
  <div class="address">PO Box 318264<br>Houston, TX 77019<br>larkmonthomes@quellmail.com</div>
  <div class="wordmark faint-mark"><span class="mark-square"></span>Larkmont Homes</div>
  <div class="side-rule"></div>
  <div class="footer">www.larkmonthomes.net</div>
</div>
<div class="piece letterhead" style="left:444px;top:17px">
  <div class="head"><div class="wordmark"><span class="mark-square"></span>Larkmont Homes</div></div>
  <div class="wordmark faint-mark"><span class="mark-square"></span>Larkmont Homes</div>
  <div class="footer">PO Box 318264 · Houston, TX 77019 · www.larkmonthomes.net</div>
</div>

<!-- flat envelopes -->
<div class="piece envelope" style="left:672px;top:43px">
  <div class="corner">
    <div class="wordmark"><span class="mark-square"></span>Larkmont Homes</div>
    <div class="return">PO Box 318264<br>Houston, TX 77019</div>
  </div>
  <div class="footer">www.larkmonthomes.net</div>
</div>
<div class="piece envelope" style="left:672px;top:156px">
  <div class="corner">
    <div class="wordmark"><span class="mark-square"></span>Larkmont Homes</div>
    <div class="return">PO Box 318264<br>Houston, TX 77019</div>
  </div>
  <div class="footer">www.larkmonthomes.net</div>
</div>

<!-- open-flap envelopes -->
<div class="flap-stack">
  <svg width="293" height="218" viewBox="0 0 293 218">
    <!-- white envelope bottom -->
    <rect x="0" y="112" width="293" height="104" fill="var(--paper)"/>
    <path d="M0 112 L146 150 L293 112" fill="none" stroke="var(--paper-edge)" stroke-width="1"/>
    <!-- grey envelope -->
    <path d="M0 60 H293 V120 L146 152 L0 120 Z" fill="var(--brand-grey)"/>
    <path d="M0 60 H293 V70 H0 Z" fill="var(--brand-grey-dark)"/>
    <!-- red envelope flap -->
    <path d="M6 4 Q146 -6 287 4 V60 L146 92 L6 60 Z" fill="var(--brand-red)"/>
    <path d="M6 4 Q146 -6 287 4 V14 Q146 4 6 14 Z" fill="var(--brand-red-dark)"/>
  </svg>
  <div class="flap-logo"><div class="wordmark on-dark"><span class="mark-square"></span>Larkmont Homes</div></div>
</div>

</body>
</html>
```